Web Site for Strategy and Technology Consulting Company

We are looking for a website design that engages potential customers to understand our services and contact us. In this contest, we are looking for a homepage design, but the winning designer will be favored for the design of some of the more complicated interior pages of the site. An additional contest (or contests) for these pages will be added soon.

PLATROM AND RESPONSIVE DESIGN
The site will be implemented in WordPress using the Elementor page builder.
We are looking for a design that will look good on phones are well as laptop browsers.

UPLOADED FILES INCLUDE:
1a A wireframe of the homepage we are looking for. The Uploaded PDF also includes a draft of the text proposed for the homepage. Designers are free to go beyond the wireframe, but all elements of the wireframe should be included.
1b A Word document with the draft text of the homepage.
2a-d The Norvalith logo. Two versions are included – a dark version which works well against a light background, and a light version which works well against a dark background.
3 The Norvalith color palette with HEX and RGB values. Designers are not limited to this palette, but colors should be complementary.
4 A draft of the homepage menu
5 Service sheets with information on the services we provide

MORE ABOUT NORVALITH
Norvalith is a consulting company focused on transforming businesses through software. Our tagline, “Transformation Delivered,” recognizes the gap business often have between business transformation and the software they end up with. By listening to our customers and understanding their vision and where they are, we help get our customers where they want to go.

We increase our capability by working with many consultants and partners, allowing us to provide our customers with the best people and the software that best suits them.

Industry/Entity Type

Consulting

Number of Pages Required

1 page

Font styles to use
Sans Serif

Requirements
Must have
• the content represented on the wireframe uploaded
Nice to have
• interactive features, such as roll-over icons that reveal additional information

```html
<!DOCTYPE html>
<html lang="en">
<head>
<meta charset="UTF-8">
<title>Norvalith — Transformation Delivered</title>
<link href="https://fonts.googleapis.com/css2?family=Sora:wght@500;600;700&family=Manrope:wght@400;500;600;700&display=swap" rel="stylesheet">
<style>
:root{
  --blue-dark:#1d5589;
  --blue:#2a6aa0;
  --blue-btn:#1f5a90;
  --yellow:#e1b912;
  --ink:#1f2328;
  --muted:#4a4f55;
  --dark:#2e2f31;
  --sky:#bcdcf0;
  --footer:#45577a;
  --line:#9aa3ad;
}
*{box-sizing:border-box;margin:0;padding:0}
html,body{width:1200px;height:3111px;overflow:hidden}
body{position:relative;font-family:'Manrope',sans-serif;color:var(--ink);background:#fff}
.abs{position:absolute}
h1,h2,h3,.brand{font-family:'Sora',sans-serif}

/* hero */
.hero{position:absolute;left:0;top:0;width:1200px;height:236px;background:linear-gradient(180deg,var(--blue-dark),var(--blue))}
.brand{color:#fff;font-weight:500;font-size:36px;letter-spacing:.5px}
.nav{display:flex;gap:26px;top:42px;left:563px;color:#fff;font-size:12.5px;font-weight:700}
.nav span::after{content:"";display:inline-block;width:6px;height:6px;border-right:2px solid #fff;border-bottom:2px solid #fff;transform:rotate(45deg);margin:0 0 3px 6px}
.btn-contact{left:980px;top:32px;width:121px;height:34px;background:var(--yellow);color:#fff;font-size:12px;font-weight:700;display:flex;align-items:center;justify-content:center}
.hero h1{left:0;width:1200px;top:104px;text-align:center;color:#fff;font-size:44px;font-weight:700}
.hero p{left:110px;width:980px;top:164px;text-align:center;color:#fff;font-size:13.5px;line-height:19px}
.pix{background:#5b8dbf;opacity:.5}

/* intro */
.intro-photo{left:520px;top:236px;width:680px;height:489px;background:linear-gradient(90deg,#ffffff 0%,#d9d4cc 18%,#b79c7c 55%,#7b6656 100%)}
.intro h2{left:132px;top:304px;font-size:26px;font-weight:600}
.checks{left:132px;top:356px;width:380px;list-style:none}
.checks li{position:relative;padding-left:27px;font-size:15px;font-weight:500;line-height:21px;margin-bottom:20px}
.checks li svg{position:absolute;left:0;top:3px}
.btn{display:flex;align-items:center;gap:8px;justify-content:center;background:var(--blue-btn);color:#fff;font-weight:700;font-size:15px}
.btn i{width:18px;height:18px;border:1.6px solid #fff;border-radius:50%;display:flex;align-items:center;justify-content:center}

/* services */
.svc-title{left:0;width:1228px;top:796px;text-align:center;font-size:35px;font-weight:600;line-height:44px}
.svc-lead{left:180px;width:860px;top:902px;text-align:center;color:var(--muted);font-size:15.5px;line-height:26px}
.card{top:1030px;width:184px;height:248px;border:1.5px solid var(--line);text-align:center;padding-top:22px}
.card h3{font-family:'Manrope',sans-serif;font-size:15.5px;font-weight:600;line-height:20px;margin-top:12px}
.card p{font-size:13px;color:var(--muted);line-height:19px;margin-top:6px;padding:0 10px;height:58px}
.card .more{margin:10px auto 0;width:116px;height:31px;border:1.5px solid var(--blue-btn);color:#7a8088;font-size:13px;display:flex;align-items:center;justify-content:center}
.card .more.on{background:var(--blue-btn);color:#fff}
.lumora{font-family:'Manrope',sans-serif;font-size:18px;font-weight:600;color:#5a5bd6;height:40px;line-height:40px}

/* people */
.people{left:0;top:1369px;width:728px;height:561px;background:var(--yellow)}
.people-photo{left:728px;top:1369px;width:472px;height:561px;background:linear-gradient(160deg,#efeeee 0%,#c9b8a4 45%,#6c5648 100%)}
.people h2{left:98px;top:1462px;font-size:34px;font-weight:600}
.people .txt{left:98px;width:580px;color:#2b2b2b;font-size:15px;line-height:26px}
.people .pts{left:98px;top:1620px;width:580px;list-style:none}
.people .pts li{position:relative;padding-left:22px;font-weight:700;font-size:15px;line-height:22px;margin-bottom:6px}
.people .pts li svg{position:absolute;left:0;top:4px}

/* testimonials */
.testi{left:0;top:1930px;width:1200px;height:544px;background:linear-gradient(180deg,#3a3b3d,#262729)}
.kicker{color:var(--yellow);font-size:15px;font-weight:700}
.testi h2{left:0;width:1200px;top:2050px;text-align:center;color:#fff;font-size:34px;font-weight:600}
.avatar{left:563px;top:2148px;width:70px;height:70px;border-radius:50%;background:linear-gradient(180deg,#e9ecef,#b9c2cc);border:3px solid #fff}
.quote{left:280px;width:640px;top:2240px;text-align:center;color:#fff;font-size:13px;line-height:21px}
.who{left:0;width:1200px;top:2318px;text-align:center;font-size:12.5px;line-height:18px}
.dots{display:flex;gap:9px;align-items:center}
.dots b{width:6px;height:6px;background:#fff}

/* technologies */
.tech h2{left:98px;top:2535px;font-size:34px;font-weight:600}
.band{left:0;top:2610px;width:1200px;height:152px;background:var(--sky)}
.logos{left:98px;top:2650px;width:1004px;display:flex;justify-content:space-between;align-items:center;height:50px}
.logos span{font-size:21px;font-weight:600;color:#4a5057;display:flex;align-items:center;gap:8px}
.logos span i{width:16px;height:16px;background:#4a5057;border-radius:50%}
.tdots{left:580px;top:2720px;display:flex;gap:6px}
.tdots b{width:6px;height:6px;border-radius:50%;background:#9cb3c7}
.tdots b.on{background:var(--blue-btn)}

/* footer */
.footer{left:0;top:2762px;width:1200px;height:349px;background:var(--footer)}
.footer .col{color:#fff;font-size:14px;line-height:22px}
.footer h4{font-family:'Sora',sans-serif;font-size:18px;font-weight:600;margin-bottom:14px}
.social{width:38px;height:38px;border:1.5px solid #fff;border-radius:50%}
.rule{left:98px;top:3023px;width:1004px;height:1px;background:#6a7a96}
.bottom{top:3060px;color:#fff;font-size:13px}
</style>
</head>
<body>

<header class="hero">
  <div class="abs brand" style="left:99px;top:24px">Norvalith</div>
  <nav class="abs nav"><span>ABOUT US</span><span>SERVICES</span><span>INSIGHTS</span><span>JOIN US</span></nav>
  <div class="abs btn-contact">CONTACT US</div>
  <h1 class="abs">Transformation Delivered.</h1>
  <p class="abs">We do more for our customers than implement software. We listen. We work to understand where they are in their transformation journey and where they want to go. We partner with them to clear the roadblocks that stand in their way, ensuring they reach their destination.</p>
  <div class="abs pix" style="left:1152px;top:148px;width:28px;height:28px"></div>
  <div class="abs pix" style="left:1096px;top:190px;width:30px;height:28px"></div>
  <div class="abs pix" style="left:1000px;top:200px;width:24px;height:24px"></div>
  <div class="abs pix" style="left:1152px;top:192px;width:22px;height:22px"></div>
</header>

<section class="intro">
  <div class="abs intro-photo" role="img" aria-label="Photo of a smiling team of five colleagues gathered around a desk with laptops"></div>
  <h2 class="abs">At Norvalith, we:</h2>
  <ul class="abs checks">
    <li><svg width="16" height="16" viewBox="0 0 16 16"><circle cx="8" cy="8" r="8" fill="#1f2328"/><path d="M4.5 8.2l2.3 2.3 4.7-4.8" stroke="#fff" stroke-width="1.8" fill="none"/></svg>Focus on business value, with an emphasis on delivering value quickly.</li>
    <li><svg width="16" height="16" viewBox="0 0 16 16"><circle cx="8" cy="8" r="8" fill="#1f2328"/><path d="M4.5 8.2l2.3 2.3 4.7-4.8" stroke="#fff" stroke-width="1.8" fill="none"/></svg>Meet our customers where they are without backing them up to the beginning of their journey.</li>
    <li><svg width="16" height="16" viewBox="0 0 16 16"><circle cx="8" cy="8" r="8" fill="#1f2328"/><path d="M4.5 8.2l2.3 2.3 4.7-4.8" stroke="#fff" stroke-width="1.8" fill="none"/></svg>Provide a wide range of services, from strategy to product support.</li>
    <li><svg width="16" height="16" viewBox="0 0 16 16"><circle cx="8" cy="8" r="8" fill="#1f2328"/><path d="M4.5 8.2l2.3 2.3 4.7-4.8" stroke="#fff" stroke-width="1.8" fill="none"/></svg>Commit to our customer’s long-term success.</li>
  </ul>
  <div class="abs btn" style="left:132px;top:618px;width:149px;height:41px">OUR STORY <i><svg width="8" height="8" viewBox="0 0 8 8"><path d="M2.5 1l3 3-3 3" stroke="#fff" stroke-width="1.4" fill="none"/></svg></i></div>
</section>

<section class="services">
  <h2 class="abs svc-title">Transformation Supported<br>by Technology</h2>
  <p class="abs svc-lead">During our early years, Norvalith focused only on business transformation. We came to realize that successful transformation often depended on quality software implementations, and often more than one. Now we focus on five things, the five things most businesses need to reach their goals.</p>

  <div class="abs card" style="left:99px">
    <svg width="40" height="40" viewBox="0 0 40 40" fill="none" stroke="#3a63c9" stroke-width="1.6"><rect x="8" y="4" width="22" height="30" rx="2"/><rect x="12" y="8" width="22" height="30" rx="2" fill="#fff"/><path d="M16 15h14M16 20h14M16 25h14M16 30h9"/></svg>
    <h3>Business<br>Transformation</h3>
    <p>Define and execute your stratege.</p>
    <div class="more">Know More</div>
  </div>
  <div class="abs card" style="left:303px">
    <svg width="40" height="40" viewBox="0 0 40 40" fill="none" stroke="#3a63c9" stroke-width="1.6"><rect x="4" y="8" width="32" height="22" rx="2"/><circle cx="20" cy="19" r="6"/><circle cx="20" cy="19" r="2"/><path d="M14 34h12M20 30v4M10 4h20"/></svg>
    <h3>ERP<br>Solutions</h3>
    <p>Assess, upgrade, and implement ERP solutions to meet your needs.</p>
    <div class="more on">Know More</div>
  </div>
  <div class="abs card" style="left:507px">
    <svg width="40" height="40" viewBox="0 0 40 40" fill="none" stroke="#3a63c9" stroke-width="1.6"><rect x="6" y="8" width="24" height="26" rx="2"/><path d="M10 14h16M10 19h12M10 24h10M6 2v8"/><circle cx="31" cy="27" r="6"/><circle cx="31" cy="27" r="2"/></svg>
    <h3>CRM<br>Solutions</h3>
    <p>Take your relationship to the next level.</p>
    <div class="more">Know More</div>
  </div>
  <div class="abs card" style="left:712px">
    <svg width="40" height="40" viewBox="0 0 40 40" fill="none" stroke="#3a63c9" stroke-width="1.6"><rect x="4" y="5" width="32" height="24" rx="2"/><path d="M10 24v-6M14 24v-10M18 24v-4M14 34h12M20 29v5"/><circle cx="27" cy="15" r="5"/><path d="M27 10v5h5"/></svg>
    <h3>Data and Business<br>Intelligence</h3>
    <p>Discover, connect, and trust your data.</p>
    <div class="more">Know More</div>
  </div>
  <div class="abs card" style="left:917px;padding-top:18px">
    <div class="lumora">Lumora</div>
    <h3 style="margin-top:10px">Building the Right<br>Team of People</h3>
    <p>Hire resources for your transfromation journey.</p>
    <div class="more">Know More</div>
  </div>
</section>

<section>
  <div class="abs people"></div>
  <div class="abs people-photo" role="img" aria-label="Photo of the consulting team smiling together at a table with a laptop and tablet"></div>
  <div class="people">
    <h2 class="abs">It’s the People</h2>
    <p class="abs txt" style="top:1524px">The world has changed in the past twenty years. The people you need might not all work for one company. Our clients want the best resources, available quickly. That’s why, in addition to our team of experts, we partner with:</p>
    <ul class="abs pts">
      <li><svg width="15" height="15" viewBox="0 0 16 16"><circle cx="8" cy="8" r="8" fill="#1f2328"/><path d="M4.5 8.2l2.3 2.3 4.7-4.8" stroke="#e1b912" stroke-width="1.8" fill="none"/></svg>A large network of expert consultants who are the best at what they do,</li>
      <li><svg width="15" height="15" viewBox="0 0 16 16"><circle cx="8" cy="8" r="8" fill="#1f2328"/><path d="M4.5 8.2l2.3 2.3 4.7-4.8" stroke="#e1b912" stroke-width="1.8" fill="none"/></svg>Service providers all over the world to provide the resources and value that are right for you, available 24 x 7.</li>
    </ul>
    <p class="abs txt" style="top:1715px">People are invariably at the center of our customer’s success. Find out how we can add our experts to yours.</p>
    <div class="abs btn" style="left:100px;top:1795px;width:148px;height:41px">OUR TEAM <i><svg width="8" height="8" viewBox="0 0 8 8"><path d="M2.5 1l3 3-3 3" stroke="#fff" stroke-width="1.4" fill="none"/></svg></i></div>
  </div>
</section>

<section>
  <div class="abs testi" role="img" aria-label="Dimmed background photo of business people in a meeting"></div>
  <div class="abs kicker" style="left:0;width:1200px;top:2022px;text-align:center">Clients Testimonials</div>
  <h2 class="abs" style="left:0;width:1200px;top:2050px;text-align:center;color:#fff;font-size:34px;font-weight:600">See What Our Clients Speak</h2>
  <div class="abs avatar" role="img" aria-label="Client portrait"></div>
  <p class="abs quote">Norvalith quickly moved us past talking about what needed to be done, to doing it. Development projects are never easy and when things got tough in the first phase of development, Norvalith stepped in to right the ship and put us on a new course.</p>
  <div class="abs who"><div style="color:#2f72b8;font-weight:700">DANA WHITFIELD, PRESIDENT</div><div style="color:var(--yellow)">Brightline Controls Co.</div></div>
  <div class="abs dots" style="left:578px;top:2384px"><b></b><b style="width:11px;height:11px;background:none;border:1.5px solid #fff;position:relative"></b><b></b></div>
</section>

<section class="tech">
  <div class="abs kicker" style="left:98px;top:2508px;font-size:14px">Technologies</div>
  <h2 class="abs">Rotator of Technologies</h2>
  <div class="abs band"></div>
  <div class="abs logos">
    <span><i></i>Corvana Suite</span>
    <span>Ledgerline</span>
    <span>Pipewell</span>
    <span>Quantora BI</span>
    <span>Frostlake</span>
    <span>Vistachart</span>
  </div>
  <div class="abs tdots"><b></b><b class="on"></b><b></b><b></b></div>
</section>

<footer>
  <div class="abs footer"></div>
  <div class="abs brand" style="left:99px;top:2826px;font-size:30px">Norvalith</div>
  <p class="abs col" style="left:100px;top:2880px;width:420px;font-size:12.5px;line-height:22px;color:#fff">We do more for our customers than implement software. We listen. We work to understand where they are in their transformation journey and where they want to go. We partner with them to clear the roadblocks that stand in their way, ensuring they reach their destination.</p>
  <div class="abs col" style="left:614px;top:2834px;width:200px">
    <h4>Address</h4>
    48 Harbor Point Way<br>Suite 210, Lakeview, MN<br>55990
  </div>
  <div class="abs social" style="left:613px;top:2953px"></div>
  <div class="abs social" style="left:659px;top:2953px"></div>
  <div class="abs col" style="left:869px;top:2834px;width:240px">
    <h4>Say Hello</h4>
    <div style="border-bottom:1px solid #fff;padding-bottom:6px;width:202px">hello@norvalithgroup.com</div>
    <div style="font-size:17px;margin-top:12px">(555) 014-2290</div>
  </div>
  <div class="abs rule"></div>
  <div class="abs bottom" style="left:98px">Offerings &nbsp;|&nbsp; Capabilities &nbsp;|&nbsp; Industries &nbsp;|&nbsp; Team &nbsp;|&nbsp; About</div>
  <div class="abs bottom" style="left:812px;width:290px;text-align:right">© 2023 Norvalith Consulting. All Rights Reserved.</div>
</footer>

</body>
</html>
```